Stationary package for Real Estate Brokerage Bramblefield Homes inc
Bramblefield Homes - Brokerage Independently Owned and Operated
Stationary package for Real Estate Brokerage Bramblefield Homes inc - Real Estate
Creative Brief
Modern
Nora Pellwick
Sales Representative
42 Fennmoor Crescent, Ottawa, ON, K2P 3T5
nora_pellwick@quillpost.example
www.norapellwick.example
Space for personal photo (head shot) in the front
Office address and extra details on the back

```html
<!DOCTYPE html>
<html lang="en">
<head>
<meta charset="utf-8">
<title>Bramblefield Homes inc – Stationery Package</title>
<link href="https://fonts.googleapis.com/css2?family=Cormorant+Garamond:ital,wght@0,600;1,500&family=Arimo:wght@400;700&display=swap" rel="stylesheet">
<style>
:root{
  --bg:#3a3a3a;
  --ink:#111111;
  --gold:#a8772a;
  --paper:#ffffff;
  --grey:#d2d2d2;
  --soft:#8a8a8a;
}
*{box-sizing:border-box;margin:0;padding:0}
html,body{width:1200px;height:254px;overflow:hidden;background:var(--bg);font-family:Arimo,Arial,sans-serif}
.canvas{position:relative;width:1200px;height:254px}
.piece{position:absolute;background:var(--paper);overflow:hidden}
.dark{background:var(--ink);color:var(--paper)}
.gold{background:var(--gold)}
.mark{display:flex;align-items:center;gap:2px;font-family:"Cormorant Garamond",Georgia,serif;font-weight:600;color:var(--ink);font-size:5px;letter-spacing:.05em;text-transform:uppercase;white-space:nowrap}
.mark .dot{width:.9em;height:.9em;border-radius:50%;background:var(--gold);flex:none}
.mark.light{color:var(--paper)}
.abs{position:absolute}
.tiny{font-size:2.4px;line-height:1.35;color:#444}
.lines{position:absolute;background:repeating-linear-gradient(to bottom,var(--grey) 0 .7px,transparent .7px 2.4px)}
.foot{position:absolute;left:0;right:0;bottom:0;height:3px;background:var(--ink)}
.foot::before{content:"";position:absolute;left:0;top:-1.2px;width:60%;height:1.2px;background:var(--gold)}
.label{position:absolute;font-size:2.6px;color:#bbb;text-align:center;font-family:Georgia,serif;white-space:nowrap}
.title-block{position:absolute;left:8px;top:30px;color:var(--paper);text-align:center;width:50px}
.title-block .sub{font-family:Georgia,serif;font-size:3.6px;margin-top:3px}
.photo{position:absolute;background:linear-gradient(#5a4a40,#2a2220);}
.disc{position:absolute;border-radius:50%;display:flex;align-items:center;justify-content:center}
.disc .hole{position:absolute;width:30%;height:30%;border-radius:50%;background:var(--paper);border:2px solid #ccc}
.slide .head{position:absolute;left:6px;top:5px;font-size:4px;font-weight:700;color:var(--ink)}
.slide .subh{position:absolute;left:6px;top:10px;font-size:2.3px;color:var(--gold)}
.slide .rule{position:absolute;left:6px;right:6px;top:13px;height:.5px;background:var(--grey)}
.script{font-family:"Cormorant Garamond",Georgia,serif;font-style:italic;font-weight:500}
.fax-row{display:flex;gap:2px;font-size:2px;color:#555;margin-bottom:1.2px}
.fax-row span{flex:1;border-bottom:.4px solid var(--grey)}
.thanks-title,.thanks-sub{position:absolute;left:0;right:0;text-align:center;color:var(--paper);font-weight:400}
</style>
</head>
<body>
<div class="canvas">

  <div class="title-block">
    <div class="mark light" style="justify-content:center;font-size:5.5px"><span class="dot"></span>Bramblefield</div>
    <div class="sub">Stationary Concepts</div>
  </div>

  <div class="piece card-front" style="left:3px;top:57px;width:48px;height:27px">
    <div class="mark abs" style="left:3px;top:3px;font-size:3.6px"><span class="dot"></span>Bramblefield</div>
    <div class="tiny abs" style="left:3px;top:10px;font-size:1.9px">42 Fennmoor Crescent<br>Ottawa, ON, K2P 3T5<br>613-555-0142<br>nora_pellwick@quillpost.example</div>
    <div class="photo" role="img" aria-label="Head shot of the sales representative" style="left:30px;top:2px;width:16px;height:17px"></div>
    <div class="abs dark" style="left:28px;top:19px;width:20px;height:8px;font-size:1.8px;padding:1px 2px;text-align:right">NORA PELLWICK<br><span style="color:var(--gold)">Sales Representative</span></div>
  </div>
  <div class="label" style="left:3px;top:85px;width:48px">Front Card</div>

  <div class="piece dark card-back" style="left:3px;top:91px;width:48px;height:27px">
    <div class="mark light abs" style="left:9px;top:9px;font-size:4.4px"><span class="dot"></span>Bramblefield</div>
    <div class="abs" style="left:0;right:0;top:20px;font-size:1.9px;text-align:center;color:#aaa">www.norapellwick.example</div>
  </div>
  <div class="label" style="left:3px;top:119px;width:48px">Back Card</div>

  <div class="piece letterhead" style="left:53px;top:15px;width:79px;height:104px">
    <div class="mark abs" style="left:6px;top:6px;font-size:4.2px"><span class="dot"></span>Bramblefield</div>
    <div class="tiny abs" style="left:55px;top:5px;font-size:1.8px">42 Fennmoor Crescent<br>Ottawa, ON<br>613-555-0142</div>
    <div class="tiny abs" style="left:6px;top:22px;font-size:1.8px">Date<br><br>Recipient Name<br>Company Name<br>Street Address<br>City, State, Zip</div>
    <div class="lines" style="left:6px;top:40px;width:66px;height:45px"></div>
    <div class="script abs" style="left:6px;top:88px;font-size:5px;color:#333">Nora Pellwick</div>
    <div class="foot"></div>
  </div>
  <div class="label" style="left:53px;top:120px;width:79px">Letterhead option_01</div>

  <div class="piece letterhead" style="left:137px;top:15px;width:79px;height:104px">
    <div class="mark abs" style="left:26px;top:6px;font-size:4.2px"><span class="dot"></span>Bramblefield</div>
    <div class="tiny abs" style="left:6px;top:22px;font-size:1.8px">Date<br><br>Recipient Name<br>Company Name<br>Street Address<br>City, State, Zip</div>
    <div class="lines" style="left:6px;top:40px;width:66px;height:45px"></div>
    <div class="script abs" style="left:6px;top:88px;font-size:5px;color:#333">Nora Pellwick</div>
    <div class="tiny abs" style="left:12px;top:97px;font-size:1.6px">42 Fennmoor Crescent, Ottawa, ON, K2P 3T5</div>
    <div class="foot"></div>
  </div>
  <div class="label" style="left:137px;top:120px;width:79px">Letterhead option_02</div>

  <div class="piece email-sig" style="left:238px;top:42px;width:52px;height:25px">
    <div class="mark abs" style="left:2px;top:3px;font-size:3.2px"><span class="dot"></span>Bramblefield</div>
    <div class="tiny abs" style="left:2px;top:9px;font-size:1.7px">Nora Pellwick<br>613-555-0142<br>www.norapellwick.example</div>
    <div class="photo" role="img" aria-label="Head shot of the sales representative" style="left:34px;top:2px;width:16px;height:16px"></div>
    <div class="abs dark" style="left:0;right:0;bottom:0;height:5px"></div>
  </div>
  <div class="label" style="left:238px;top:68px;width:52px">Email Signature</div>

  <div class="piece envelope" style="left:220px;top:80px;width:85px;height:36px">
    <div class="mark abs" style="left:3px;top:3px;font-size:3.4px"><span class="dot"></span>Bramblefield</div>
    <div class="tiny abs" style="left:3px;top:9px;font-size:1.6px">42 Fennmoor Crescent, Ottawa, ON</div>
    <div class="foot"></div>
  </div>
  <div class="label" style="left:220px;top:117px;width:85px">Envelope_Front</div>

  <div class="piece envelope-back" style="left:308px;top:40px;width:90px;height:76px">
    <div class="abs dark" style="left:0;right:0;top:0;height:12px"></div>
    <div class="abs gold" style="left:0;right:0;top:20px;height:14px"></div>
    <div class="abs" style="left:42px;top:42px;width:6px;height:6px;border-radius:50%;background:var(--gold)"></div>
    <div class="abs" style="left:0;right:0;top:50px;font-size:1.8px;color:#888;text-align:center">www.norapellwick.example</div>
  </div>
  <div class="label" style="left:308px;top:117px;width:90px">Envelope_Back</div>

  <div class="piece folder" style="left:410px;top:18px;width:124px;height:100px;background:transparent">
    <div class="abs dark" style="left:0;top:0;width:62px;height:100px"></div>
    <div class="abs gold" style="left:0;top:0;width:2px;height:100px"></div>
    <div class="abs" style="left:62px;top:0;width:62px;height:100px;background:var(--paper)"></div>
    <div class="mark abs" style="left:72px;top:32px;font-size:5.2px"><span class="dot"></span>Bramblefield</div>
    <div class="tiny abs" style="left:5px;top:62px;font-size:1.7px;color:#aaa">42 Fennmoor Crescent<br>Ottawa, ON, K2P 3T5<br>613-555-0142</div>
    <div class="abs gold" style="left:62px;right:0;bottom:0;height:3px"></div>
  </div>
  <div class="label" style="left:410px;top:119px;width:124px">Folder</div>

  <div class="piece fax" style="left:539px;top:15px;width:79px;height:104px">
    <div class="mark abs" style="left:6px;top:6px;font-size:4px"><span class="dot"></span>Bramblefield</div>
    <div class="abs" style="left:6px;top:20px;width:67px">
      <div class="fax-row">To<span></span>From<span></span></div>
      <div class="fax-row">Fax<span></span>Pages<span></span></div>
      <div class="fax-row">Phone<span></span>Date<span></span></div>
      <div class="fax-row">Re<span></span>CC<span></span></div>
      <div class="fax-row" style="margin-top:3px">□ Urgent □ Review □ Reply</div>
      <div class="fax-row">Comments:</div>
    </div>
    <div class="foot"></div>
  </div>
  <div class="label" style="left:539px;top:120px;width:79px">Fax option_01</div>

  <div class="piece fax" style="left:622px;top:15px;width:79px;height:104px">
    <div class="mark abs" style="left:28px;top:6px;font-size:4px"><span class="dot"></span>Bramblefield</div>
    <div class="abs" style="left:6px;top:20px;width:67px">
      <div class="fax-row">To<span></span>From<span></span></div>
      <div class="fax-row">Fax<span></span>Pages<span></span></div>
      <div class="fax-row">Phone<span></span>Date<span></span></div>
      <div class="fax-row">Re<span></span>CC<span></span></div>
      <div class="fax-row" style="margin-top:3px">□ Urgent □ Review □ Reply</div>
      <div class="fax-row">Comments:</div>
    </div>
    <div class="foot"></div>
  </div>
  <div class="label" style="left:622px;top:120px;width:79px">Fax option_02</div>

  <div class="piece slip" style="left:715px;top:27px;width:85px;height:34px">
    <div class="mark abs" style="left:4px;top:4px;font-size:3.4px"><span class="dot"></span>Bramblefield</div>
    <div class="script abs" style="left:20px;top:17px;font-size:7px;color:#333">With Compliments</div>
    <div class="foot"></div>
  </div>
  <div class="label" style="left:715px;top:63px;width:85px">Compliment Slip</div>

  <div class="piece thanks-front" style="left:708px;top:72px;width:55px;height:37px">
    <div class="mark abs" style="left:3px;top:4px;font-size:3px"><span class="dot"></span>Bramblefield</div>
    <div class="script abs" style="left:8px;top:17px;font-size:8px;color:#222">Thank you</div>
    <div class="foot"></div>
  </div>
  <div class="label" style="left:708px;top:110px;width:55px">Thank You Card_Front</div>

  <div class="piece dark thanks-back" style="left:766px;top:72px;width:55px;height:37px">
    <div class="tiny abs" style="left:3px;bottom:4px;font-size:1.6px;color:#aaa">42 Fennmoor Crescent, Ottawa, ON</div>
  </div>
  <div class="label" style="left:766px;top:110px;width:55px">Thank You Card_Back</div>

  <div class="disc dark" style="left:815px;top:4px;width:58px;height:58px">
    <div class="mark light abs" style="top:8px;font-size:3.4px"><span class="dot"></span>Bramblefield</div>
    <div class="hole" style="border-color:#333"></div>
  </div>
  <div class="label" style="left:815px;top:64px;width:58px">CD</div>

  <div class="piece cd-cover" style="left:878px;top:10px;width:58px;height:50px">
    <div class="abs dark" style="left:0;right:0;top:0;height:5px"></div>
    <div class="mark abs" style="left:4px;top:10px;font-size:3.4px"><span class="dot"></span>Bramblefield</div>
    <div class="foot"></div>
  </div>
  <div class="label" style="left:878px;top:62px;width:58px">CD cover</div>

  <div class="piece dark tablet-screen" style="left:815px;top:71px;width:58px;height:44px">
    <div class="mark light abs" style="left:13px;top:18px;font-size:4.2px"><span class="dot"></span>Bramblefield</div>
  </div>
  <div class="label" style="left:815px;top:117px;width:58px">Tablet</div>

  <div class="piece phone-screen" style="left:886px;top:74px;width:17px;height:36px">
    <div class="mark abs" style="left:-6px;top:15px;font-size:2.6px;transform:rotate(-90deg)"><span class="dot"></span>Bramblefield</div>
  </div>
  <div class="piece dark phone-screen" style="left:910px;top:74px;width:17px;height:36px">
    <div class="mark light abs" style="left:-6px;top:15px;font-size:2.6px;transform:rotate(-90deg)"><span class="dot"></span>Bramblefield</div>
  </div>
  <div class="label" style="left:884px;top:112px;width:21px">Phone_01</div>
  <div class="label" style="left:908px;top:112px;width:21px">Phone_02</div>

  <div class="piece folder-inner" style="left:476px;top:140px;width:125px;height:74px">
    <div class="abs gold" style="left:0;top:0;width:3px;height:74px"></div>
    <div class="abs gold" style="right:0;top:0;width:3px;height:74px"></div>
    <div class="abs dark" style="left:8px;right:8px;bottom:0;height:24px;clip-path:polygon(0 25%,35% 0,50% 30%,65% 0,100% 25%,100% 100%,0 100%)"></div>
  </div>
  <div class="label" style="left:476px;top:215px;width:125px">Folder Inner</div>

  <div class="disc" style="left:485px;top:223px;width:20px;height:20px;background:var(--paper);border:1px solid var(--gold)"><div class="mark" style="font-size:2px">Bramblefield</div></div>
  <div class="disc dark" style="left:510px;top:223px;width:20px;height:20px"><span style="width:5px;height:5px;border-radius:50%;background:var(--gold)"></span></div>
  <div class="disc gold" style="left:535px;top:223px;width:20px;height:20px"><span style="width:5px;height:5px;border-radius:50%;background:var(--paper)"></span></div>
  <div class="disc" style="left:560px;top:223px;width:20px;height:20px;background:var(--paper);border:1px solid #999"><div class="mark" style="font-size:2px">Bramblefield</div></div>
  <div class="label" style="left:485px;top:245px;width:95px">Car Magnet</div>

  <div class="disc dark" style="left:683px;top:128px;width:56px;height:56px"><div class="mark light abs" style="top:6px;font-size:3.2px"><span class="dot"></span>Bramblefield</div><div class="hole"></div></div>
  <div class="disc gold" style="left:748px;top:128px;width:56px;height:56px"><div class="mark light abs" style="top:6px;font-size:3.2px"><span class="dot" style="background:var(--paper)"></span>Bramblefield</div><div class="hole"></div></div>
  <div class="disc" style="left:683px;top:190px;width:56px;height:56px;background:var(--paper);border:1px solid #999"><div class="mark abs" style="top:6px;font-size:3.2px"><span class="dot"></span>Bramblefield</div><div class="hole" style="border-color:var(--ink)"></div></div>
  <div class="disc dark" style="left:748px;top:190px;width:56px;height:56px;border:1.5px solid var(--paper)"><div class="mark light abs" style="top:6px;font-size:3.2px"><span class="dot"></span>Bramblefield</div><div class="hole"></div></div>
  <div class="label" style="left:683px;top:247px;width:121px">CD</div>

  <div class="piece dark cd-cover" style="left:820px;top:143px;width:58px;height:40px">
    <div class="mark light abs" style="left:4px;top:5px;font-size:3.2px"><span class="dot"></span>Bramblefield</div>
  </div>
  <div class="label" style="left:820px;top:185px;width:58px">CD cover</div>
  <div class="piece cd-cover" style="left:820px;top:196px;width:58px;height:40px">
    <div class="mark abs" style="left:4px;top:5px;font-size:3.2px"><span class="dot"></span>Bramblefield</div>
  </div>
  <div class="label" style="left:820px;top:238px;width:58px">CD cover</div>

  <div class="piece tablet-screen" style="left:894px;top:145px;width:50px;height:38px">
    <div class="mark abs" style="left:9px;top:16px;font-size:3.8px"><span class="dot"></span>Bramblefield</div>
  </div>
  <div class="label" style="left:894px;top:185px;width:50px">Tablet</div>
  <div class="piece dark tablet-screen" style="left:894px;top:198px;width:50px;height:38px">
    <div class="mark light abs" style="left:9px;top:16px;font-size:3.8px"><span class="dot"></span>Bramblefield</div>
  </div>
  <div class="label" style="left:894px;top:238px;width:50px">Tablet</div>

  <div class="piece phone-screen" style="left:962px;top:145px;width:16px;height:36px">
    <div class="mark abs" style="left:-7px;top:15px;font-size:2.4px;transform:rotate(-90deg)"><span class="dot"></span>Bramblefield</div>
  </div>
  <div class="label" style="left:958px;top:185px;width:24px">Phone_03</div>
  <div class="piece phone-screen" style="left:962px;top:198px;width:16px;height:36px">
    <div class="mark abs" style="left:-7px;top:15px;font-size:2.4px;transform:rotate(-90deg)"><span class="dot"></span>Bramblefield</div>
  </div>
  <div class="label" style="left:958px;top:238px;width:24px">Phone_04</div>

  <div class="piece slide" style="left:1002px;top:13px;width:94px;height:66px">
    <div class="mark abs" style="left:18px;top:16px;font-size:7px"><span class="dot"></span>Bramblefield</div>
    <div class="abs" style="left:0;right:0;top:42px;text-align:center;font-size:4px;color:var(--gold)">Welcome to Our</div>
    <div class="abs" style="left:0;right:0;top:47px;text-align:center;font-size:4.6px;font-weight:700;color:var(--ink)">Presentation Name</div>
    <div class="abs" style="left:0;right:0;top:53px;text-align:center;font-size:3.4px;color:var(--gold)">Description</div>
    <div class="foot"></div>
  </div>
  <div class="piece slide" style="left:1101px;top:13px;width:94px;height:66px">
    <div class="head">Heading Here</div><div class="subh">Sub Heading</div><div class="rule"></div>
    <div class="abs" style="left:6px;top:20px;width:82px;display:flex;gap:3px">
      <div style="flex:1;height:17px;background:#777;font-size:2px;color:#ddd;display:flex;align-items:center;justify-content:center">Photo</div>
      <div style="flex:1;height:17px;background:#777;font-size:2px;color:#ddd;display:flex;align-items:center;justify-content:center">Photo</div>
      <div style="flex:1;height:17px;background:#777;font-size:2px;color:#ddd;display:flex;align-items:center;justify-content:center">Photo</div>
      <div style="flex:1;height:17px;background:#777;font-size:2px;color:#ddd;display:flex;align-items:center;justify-content:center">Photo</div>
    </div>
    <div class="abs tiny" style="left:6px;top:40px;width:82px;display:flex;gap:3px;font-size:1.8px"><span style="flex:1">Team member1</span><span style="flex:1">Team member2</span><span style="flex:1">Team member3</span><span style="flex:1">Team member4</span></div>
    <div class="foot"></div>
  </div>

  <div class="piece slide" style="left:1002px;top:88px;width:94px;height:68px">
    <div class="head">Heading Here</div><div class="subh">Sub Heading</div><div class="rule"></div>
    <div class="tiny abs" style="left:6px;top:17px;font-size:2px;font-weight:700;color:var(--ink)">Group1</div>
    <div class="lines" style="left:6px;top:20px;width:38px;height:8px"></div>
    <div class="tiny abs" style="left:6px;top:30px;font-size:2px;font-weight:700;color:var(--ink)">Group2</div>
    <div class="lines" style="left:6px;top:33px;width:38px;height:8px"></div>
    <div class="tiny abs" style="left:6px;top:43px;font-size:2px;font-weight:700;color:var(--ink)">Group3</div>
    <div class="lines" style="left:6px;top:46px;width:38px;height:8px"></div>
    <div class="tiny abs" style="left:50px;top:17px;font-size:2px;font-weight:700;color:var(--ink)">Group4</div>
    <div class="lines" style="left:50px;top:20px;width:38px;height:8px"></div>
    <div class="tiny abs" style="left:50px;top:30px;font-size:2px;font-weight:700;color:var(--ink)">Group5</div>
    <div class="lines" style="left:50px;top:33px;width:38px;height:8px"></div>
    <div class="tiny abs" style="left:50px;top:43px;font-size:2px;font-weight:700;color:var(--ink)">Group6</div>
    <div class="lines" style="left:50px;top:46px;width:38px;height:8px"></div>
    <div class="foot"></div>
  </div>
  <div class="piece slide" style="left:1101px;top:88px;width:94px;height:68px">
    <div class="head">Heading Here</div><div class="subh">Sub Heading</div><div class="rule"></div>
    <svg class="abs" style="left:6px;top:18px" width="40" height="36" viewBox="0 0 40 36">
      <line x1="1" y1="35" x2="39" y2="35" stroke="#999" stroke-width=".5"/>
      <rect x="4" y="6" width="5" height="29" fill="#111"/>
      <rect x="11" y="11" width="5" height="24" fill="#111"/>
      <rect x="18" y="14" width="5" height="21" fill="#111"/>
      <rect x="25" y="18" width="5" height="17" fill="#111"/>
      <rect x="32" y="22" width="5" height="13" fill="#111"/>
    </svg>
    <div class="lines" style="left:52px;top:18px;width:36px;height:34px"></div>
    <div class="foot"></div>
  </div>

  <div class="piece slide" style="left:1002px;top:165px;width:94px;height:68px">
    <div class="head">Heading Here</div><div class="subh">Sub Heading</div><div class="rule"></div>
    <div class="lines" style="left:6px;top:18px;width:40px;height:40px"></div>
    <svg class="abs" style="left:58px;top:20px" width="24" height="24" viewBox="0 0 24 24">
      <circle cx="12" cy="12" r="11" fill="#111"/>
      <path d="M12 12 L12 1 A11 11 0 0 1 22.5 15 Z" fill="#a8772a"/>
      <path d="M12 12 L22.5 15 A11 11 0 0 1 14 22.8 Z" fill="#fff"/>
    </svg>
    <div class="tiny abs" style="left:54px;top:48px;font-size:1.8px">■ Lorem ipsum dolor<br>■ Sit amet elit</div>
    <div class="foot"></div>
  </div>
  <div class="piece dark slide" style="left:1101px;top:165px;width:94px;height:68px">
    <div class="thanks-title" style="top:22px;font-size:13px">Thanks</div>
    <div class="thanks-sub" style="top:37px;font-size:7.5px">For Coming</div>
    <div class="abs" style="left:0;right:0;bottom:5px;text-align:center;font-size:1.7px;color:#aaa">42 Fennmoor Crescent, Ottawa, ON, K2P 3T5 · nora_pellwick@quillpost.example</div>
  </div>

</div>
</body>
</html>
```